Mosque App design fresh look and feel

Need to create a mosque app which has half a couple of dozen pages, a login page will take you into the main information with about 6 categories, such as school, memberships, information, prayer times etc... we have 3 types of users... 1. User .. admin user 3. imam user

I have xd files available.
https://mocks.plarvio.com/view/e4f7a2d1-8b3c-4f6e-a9d2-71b5c3e8f046-2ac7/

Target Market(s)

Muslims

Font styles to use
Sans Serif

Requirements
Must have
• Great UI
Simple flow

```html
<!DOCTYPE html>
<html lang="en">
<head>
<meta charset="utf-8">
<title>Mosque App – Approve Children &amp; Total Donated</title>
<link rel="stylesheet" href="https://fonts.googleapis.com/css2?family=Poppins:wght@400;500;600&display=swap">
<style>
  :root {
    --teal: #52d6b6;
    --teal-dark: #006b56;
    --ink: #0b5a48;
    --muted: #7c8a86;
    --white: #ffffff;
    --bg: #ffffff;
    --line: #52d6b6;
  }
  * { box-sizing: border-box; margin: 0; padding: 0; }
  html, body { width: 1200px; height: 1123px; overflow: hidden; background: var(--bg); }
  body { position: relative; font-family: "Poppins", sans-serif; color: var(--ink); }

  .screen {
    position: absolute; top: 67px; width: 457px; height: 988px;
    background: var(--white); border-radius: 17px; overflow: hidden;
    box-shadow: 0 12px 22px rgba(0,0,0,.16);
  }
  .screen--approve { left: 100px; }
  .screen--donated { left: 644px; }

  .app-bar { position: absolute; left: 0; top: 0; width: 100%; height: 130px; background: var(--teal); }
  .app-bar__menu { position: absolute; left: 37px; top: 43px; }
  .app-bar__bell { position: absolute; left: 356px; top: 41px; }
  .app-bar__chat { position: absolute; left: 396px; top: 42px; }
  .app-bar__title {
    position: absolute; left: 0; right: 0; top: 84px; text-align: center;
    color: var(--white); font-weight: 600; font-size: 17px; letter-spacing: -.2px;
  }

  .avatar {
    position: absolute; left: 36px; width: 68px; height: 68px; border-radius: 50%;
    background: linear-gradient(160deg, #b89a86 0%, #6d4a3c 60%, #3a2a24 100%);
  }
  .avatar--soft { background: linear-gradient(160deg, #e9ddd6 0%, #b7957f 60%, #6e5448 100%); }
  .avatar--red { background: linear-gradient(160deg, #d9c3b8 0%, #a2553d 55%, #5a2f25 100%); box-shadow: 0 6px 12px rgba(82,214,182,.35); }
  .avatar--light { background: linear-gradient(160deg, #f1ece8 0%, #d7b9a1 60%, #8b6a53 100%); }

  .child-card {
    position: absolute; left: 136px; width: 284px; height: 67px; background: var(--white);
    box-shadow: 0 2px 6px rgba(0,0,0,.18);
  }
  .child-card--open { height: 134px; box-shadow: none; border: 1px solid var(--line); }
  .child-card__name { position: absolute; left: 17px; top: 10px; font-size: 13px; font-weight: 500; }
  .child-card__place { position: absolute; left: 17px; top: 36px; font-size: 11.5px; }
  .child-card__status {
    position: absolute; right: 10px; top: 11px; font-size: 10px; display: flex; align-items: center; gap: 4px;
  }
  .child-card__status::before { content: ""; width: 9px; height: 9px; border-radius: 50%; background: var(--teal); }
  .child-card__status--plain::before { display: none; }
  .child-card__toggle {
    position: absolute; right: 9px; bottom: 6px; width: 17px; height: 17px; border-radius: 50%;
    background: var(--white); box-shadow: 0 1px 3px rgba(0,0,0,.25);
    display: flex; align-items: center; justify-content: center;
  }
  .detail { position: absolute; left: 17px; font-size: 11.5px; display: flex; }
  .detail__label { width: 91px; color: var(--muted); }
  .detail__value { font-weight: 500; }

  .btn-approve {
    position: absolute; left: 295px; top: 733px; width: 125px; height: 43px; background: var(--teal);
    color: var(--white); font-weight: 600; font-size: 15px; display: flex; align-items: center; justify-content: center;
    box-shadow: 0 3px 6px rgba(0,0,0,.15);
  }

  .pill {
    position: absolute; width: 117px; height: 45px; display: flex; align-items: center; justify-content: center;
    font-size: 11.5px; font-weight: 500;
  }
  .pill--select { background: var(--teal); color: var(--white); font-size: 14.5px; font-weight: 600; top: 167px; gap: 0; }
  .pill--select .pill__arrow {
    position: absolute; right: 9px; top: 14px; width: 17px; height: 17px; border-radius: 50%;
    background: var(--white); display: flex; align-items: center; justify-content: center;
  }
  .pill--cell { border: 1.5px solid var(--line); color: var(--ink); }

  .nav-bar { position: absolute; left: 0; top: 915px; width: 100%; height: 73px; background: var(--teal); }
  .nav-bar__icon { position: absolute; top: 19px; }
  .nav-bar__active {
    position: absolute; top: 14px; height: 46px; background: var(--teal-dark); color: var(--white);
    display: flex; align-items: center; justify-content: center; gap: 9px; font-size: 14px; font-weight: 600;
  }
</style>
</head>
<body>

<!-- Approve Children -->
<section class="screen screen--approve">
  <header class="app-bar">
    <svg class="app-bar__menu" width="27" height="22" viewBox="0 0 27 22"><g fill="var(--teal-dark)"><rect width="22" height="4" rx="2"/><rect y="9" width="14" height="4" rx="2"/><rect y="18" width="27" height="4" rx="2"/></g></svg>
    <svg class="app-bar__bell" width="26" height="24" viewBox="0 0 26 24"><path fill="var(--teal-dark)" d="M13 2a2 2 0 0 1 2 2v.6A7 7 0 0 1 20 11v5l2 2v1H4v-1l2-2v-5a7 7 0 0 1 5-6.4V4a2 2 0 0 1 2-2zm-3 18h6a3 3 0 0 1-6 0zM3 4l2 1.5A9 9 0 0 0 2.5 11H0.5A11 11 0 0 1 3 4zm20 0a11 11 0 0 1 2.5 7h-2A9 9 0 0 0 21 5.5z"/></svg>
    <svg class="app-bar__chat" width="24" height="22" viewBox="0 0 24 22"><path fill="var(--teal-dark)" d="M2 0h20a2 2 0 0 1 2 2v13a2 2 0 0 1-2 2H6l-6 5V2a2 2 0 0 1 2-2z"/><g fill="var(--teal)"><rect x="5" y="4" width="14" height="2"/><rect x="5" y="8" width="14" height="2"/><rect x="5" y="12" width="9" height="2"/></g></svg>
    <h1 class="app-bar__title">Approve Children</h1>
  </header>

  <div class="avatar" style="top:191px" role="img" aria-label="Profile photo of a boy"></div>
  <article class="child-card" style="top:191px">
    <p class="child-card__name">Fulan</p>
    <p class="child-card__status">Online 2 hours ago</p>
    <p class="child-card__place">New Delhi, India</p>
    <span class="child-card__toggle"><svg width="9" height="6" viewBox="0 0 9 6"><path d="M1 1l3.5 3.5L8 1" fill="none" stroke="var(--ink)" stroke-width="1.2"/></svg></span>
  </article>

  <div class="avatar avatar--soft" style="top:302px" role="img" aria-label="Profile photo of a girl"></div>
  <article class="child-card" style="top:302px">
    <p class="child-card__name">Fulana</p>
    <p class="child-card__status">Online</p>
    <p class="child-card__place">Islamabad, Pakistan</p>
    <span class="child-card__toggle"><svg width="9" height="6" viewBox="0 0 9 6"><path d="M1 1l3.5 3.5L8 1" fill="none" stroke="var(--ink)" stroke-width="1.2"/></svg></span>
  </article>

  <div class="avatar avatar--red" style="top:413px" role="img" aria-label="Profile photo of a girl"></div>
  <article class="child-card child-card--open" style="top:413px">
    <p class="child-card__name">Fulana</p>
    <p class="child-card__status child-card__status--plain" style="top:8px">Islamabad, Pakistan</p>
    <p class="child-card__status" style="top:23px">Online</p>
    <p class="detail" style="top:43px"><span class="detail__label">Gender</span><span class="detail__value">Girl</span></p>
    <p class="detail" style="top:68px"><span class="detail__label">Age</span><span class="detail__value">16</span></p>
    <p class="detail" style="top:94px"><span class="detail__label">Quran Level</span><span class="detail__value">Superior</span></p>
    <span class="child-card__toggle"><svg width="9" height="6" viewBox="0 0 9 6"><path d="M1 5l3.5-3.5L8 5" fill="none" stroke="var(--ink)" stroke-width="1.2"/></svg></span>
  </article>

  <div class="avatar avatar--light" style="top:592px" role="img" aria-label="Profile photo of a boy"></div>
  <article class="child-card" style="top:592px">
    <p class="child-card__name">Fulan</p>
    <p class="child-card__status">Online 2 hours ago</p>
    <p class="child-card__place">New Delhi, India</p>
    <span class="child-card__toggle"><svg width="9" height="6" viewBox="0 0 9 6"><path d="M1 1l3.5 3.5L8 1" fill="none" stroke="var(--ink)" stroke-width="1.2"/></svg></span>
  </article>

  <div class="btn-approve">Approve</div>

  <nav class="nav-bar">
    <svg class="nav-bar__icon" style="left:38px" width="34" height="32" viewBox="0 0 34 32"><path fill="var(--teal-dark)" d="M17 1L1 16h5v15h8v-10h6v10h8V16h5z"/></svg>
    <svg class="nav-bar__icon" style="left:152px" width="34" height="34" viewBox="0 0 34 34"><circle cx="17" cy="17" r="14.5" fill="none" stroke="var(--teal-dark)" stroke-width="3"/><path d="M17 8v10l6 4" fill="none" stroke="var(--teal-dark)" stroke-width="3" stroke-linecap="round"/></svg>
    <div class="nav-bar__active" style="left:242px;width:105px">
      <svg width="32" height="28" viewBox="0 0 32 28"><g fill="none" stroke="var(--white)" stroke-width="3" stroke-linecap="round"><path d="M1 4l3 3 5-6"/><path d="M1 14l3 3 5-6"/><path d="M13 4h18M13 14h18M13 24h18"/></g><circle cx="4" cy="24" r="2.5" fill="var(--white)"/></svg>
      Task
    </div>
    <svg class="nav-bar__icon" style="left:386px" width="34" height="34" viewBox="0 0 34 34"><circle cx="17" cy="17" r="16" fill="var(--teal-dark)"/><circle cx="17" cy="13" r="5.5" fill="var(--teal)"/><path d="M7 27a11 8 0 0 1 20 0a14 14 0 0 1-20 0z" fill="var(--teal)"/></svg>
  </nav>
</section>

<!-- Total Donated -->
<section class="screen screen--donated">
  <header class="app-bar">
    <svg class="app-bar__menu" width="27" height="22" viewBox="0 0 27 22"><g fill="var(--teal-dark)"><rect width="22" height="4" rx="2"/><rect y="9" width="14" height="4" rx="2"/><rect y="18" width="27" height="4" rx="2"/></g></svg>
    <svg class="app-bar__bell" width="26" height="24" viewBox="0 0 26 24"><path fill="var(--teal-dark)" d="M13 2a2 2 0 0 1 2 2v.6A7 7 0 0 1 20 11v5l2 2v1H4v-1l2-2v-5a7 7 0 0 1 5-6.4V4a2 2 0 0 1 2-2zm-3 18h6a3 3 0 0 1-6 0zM3 4l2 1.5A9 9 0 0 0 2.5 11H0.5A11 11 0 0 1 3 4zm20 0a11 11 0 0 1 2.5 7h-2A9 9 0 0 0 21 5.5z"/></svg>
    <svg class="app-bar__chat" width="24" height="22" viewBox="0 0 24 22"><path fill="var(--teal-dark)" d="M2 0h20a2 2 0 0 1 2 2v13a2 2 0 0 1-2 2H6l-6 5V2a2 2 0 0 1 2-2z"/><g fill="var(--teal)"><rect x="5" y="4" width="14" height="2"/><rect x="5" y="8" width="14" height="2"/><rect x="5" y="12" width="9" height="2"/></g></svg>
    <h1 class="app-bar__title" style="top:81px">Total Donated</h1>
  </header>

  <div class="pill pill--select" style="left:37px;padding-right:22px">January<span class="pill__arrow"><svg width="9" height="6" viewBox="0 0 9 6"><path d="M1 1l3.5 3.5L8 1" fill="none" stroke="var(--teal)" stroke-width="1.4"/></svg></span></div>
  <div class="pill pill--select" style="left:303px;padding-right:14px">2021<span class="pill__arrow"><svg width="9" height="6" viewBox="0 0 9 6"><path d="M1 1l3.5 3.5L8 1" fill="none" stroke="var(--teal)" stroke-width="1.4"/></svg></span></div>

  <div class="pill pill--cell" style="left:37px;top:235px">Jan 27 - 4.00 PM</div>
  <div class="pill pill--cell" style="left:171px;top:235px">Lorem Ipsum</div>
  <div class="pill pill--cell" style="left:305px;top:235px">$5000</div>

  <div class="pill pill--cell" style="left:37px;top:304px">Jan 27 - 4.00 PM</div>
  <div class="pill pill--cell" style="left:171px;top:304px">Lorem Ipsum</div>
  <div class="pill pill--cell" style="left:305px;top:304px">$5000</div>

  <div class="pill pill--cell" style="left:37px;top:374px">Jan 27 - 4.00 PM</div>
  <div class="pill pill--cell" style="left:171px;top:374px">Lorem Ipsum</div>
  <div class="pill pill--cell" style="left:305px;top:374px">$5000</div>

  <div class="pill pill--cell" style="left:37px;top:443px">Jan 27 - 4.00 PM</div>
  <div class="pill pill--cell" style="left:171px;top:443px">Lorem Ipsum</div>
  <div class="pill pill--cell" style="left:305px;top:443px">$5000</div>

  <div class="pill pill--cell" style="left:37px;top:513px">Jan 27 - 4.00 PM</div>
  <div class="pill pill--cell" style="left:171px;top:513px">Lorem Ipsum</div>
  <div class="pill pill--cell" style="left:305px;top:513px">$5000</div>

  <nav class="nav-bar">
    <svg class="nav-bar__icon" style="left:37px" width="34" height="32" viewBox="0 0 34 32"><path fill="var(--teal-dark)" d="M17 1L1 16h5v15h8v-10h6v10h8V16h5z"/></svg>
    <svg class="nav-bar__icon" style="left:136px" width="34" height="34" viewBox="0 0 34 34"><circle cx="17" cy="17" r="14.5" fill="none" stroke="var(--teal-dark)" stroke-width="3"/><path d="M17 8v10l6 4" fill="none" stroke="var(--teal-dark)" stroke-width="3" stroke-linecap="round"/></svg>
    <svg class="nav-bar__icon" style="left:236px;top:22px" width="32" height="28" viewBox="0 0 32 28"><g fill="none" stroke="var(--teal-dark)" stroke-width="3" stroke-linecap="round"><path d="M1 4l3 3 5-6"/><path d="M1 14l3 3 5-6"/><path d="M13 4h18M13 14h18M13 24h18"/></g><circle cx="4" cy="24" r="2.5" fill="var(--teal-dark)"/></svg>
    <div class="nav-bar__active" style="left:309px;width:111px;gap:7px">
      <svg width="32" height="32" viewBox="0 0 34 34"><circle cx="17" cy="17" r="16" fill="var(--white)"/><circle cx="17" cy="13" r="5.5" fill="var(--teal-dark)"/><path d="M7 27a11 8 0 0 1 20 0a14 14 0 0 1-20 0z" fill="var(--teal-dark)"/></svg>
      Account
    </div>
  </nav>
</section>

</body>
</html>
```